Website for Youth Orchestra to sell tickets and attract young musicians

We are looking for a new website design for a Youth Orchestra; one of the best classical youth orchestras in the county. This project is the design only. <br/><br/>The website serves two main purposes:<br/>• Selling tickets for concerts and performances of the orchestra<br/>• Recruiting young musicians to do audition for the orchestra<br/>
Updates

Target Market(s)

Classical music lovers with a special interest in young upcoming musicians.
Young talented musicians

Number of Pages Required

2 page

Colors
ec1f27

Requirements
Must have
• - A Picture on the front page that promotes the main upcomming event
• - Attention for recruiting new musicians
• - Pictures with young musicians (white back ground, see examples)
• - Responsive
• - Please use the logo attached
Should not have
• The brown colors of the current website (kvb-veldhorst.example)

```html
<!DOCTYPE html>
<html lang="en">
<head>
<meta charset="utf-8">
<title>Eemstad Jeugdorkest — A Classical youth orchestra</title>
<link href="https://fonts.googleapis.com/css2?family=Poppins:wght@300;400;500;600;700&family=Roboto+Slab:wght@400&display=swap" rel="stylesheet">
<style>
:root{
  --red:#ec1f27;
  --red-deep:#6e1a22;
  --ink:#17161f;
  --ink-2:#1f1e2a;
  --text:#ffffff;
  --muted:#b9b7c4;
  --card-text:#2a2a33;
  --card-muted:#8a8894;
  --line:rgba(255,255,255,.18);
}
*{box-sizing:border-box;margin:0;padding:0}
html,body{width:1200px;height:3004px;overflow:hidden}
body{font-family:'Poppins',sans-serif;color:var(--text);background:linear-gradient(180deg,var(--ink-2) 0%,var(--ink) 60%,#101016 100%);position:relative}
.abs{position:absolute}
a{color:inherit;text-decoration:none}

/* header */
.site-header{position:absolute;left:0;top:0;width:1200px;height:88px;z-index:3}
.brand{position:absolute;left:22px;top:8px;display:flex;align-items:center;gap:10px}
.brand-dot{width:58px;height:58px;border-radius:50%;background:var(--red)}
.brand-name{font-weight:600;font-size:15px;color:#fff;line-height:1.15;width:110px}
.main-nav{position:absolute;left:326px;top:26px;display:flex;gap:26px;font-size:13px;font-weight:400}
.main-nav a{position:relative;padding-bottom:8px;color:rgba(255,255,255,.9)}
.main-nav a.active{color:#fff;font-weight:500}
.main-nav a.active::after{content:"";position:absolute;left:-8px;right:-8px;bottom:-6px;height:3px;background:var(--red)}

/* hero */
.hero{position:absolute;left:0;top:0;width:1200px;height:660px;overflow:hidden}
.hero-photo{position:absolute;inset:0;background:
  radial-gradient(ellipse at 50% 8%,rgba(236,31,39,.55),transparent 55%),
  linear-gradient(180deg,#a61d3f 0%,#7a1c45 35%,#3d1a3e 72%,#1f1e2a 100%)}
.hero-eyebrow{position:absolute;left:0;width:1200px;top:184px;text-align:center;font-size:11px;letter-spacing:.5px;color:rgba(255,255,255,.75)}
.hero-title{position:absolute;left:0;width:1200px;top:214px;text-align:center;font-size:50px;font-weight:600;line-height:1.22}
.hero-title em{font-style:normal;color:var(--red)}
.hero-text{position:absolute;left:390px;width:420px;top:338px;text-align:center;font-size:14px;line-height:1.6;color:rgba(255,255,255,.85)}
.btn{position:absolute;height:42px;border-radius:21px;display:flex;align-items:center;justify-content:center;gap:8px;font-size:13px;font-weight:500}
.btn-red{background:var(--red);color:#fff}
.btn-white{background:#fff;color:var(--red)}

/* ghost words */
.ghost{position:absolute;font-weight:700;color:rgba(255,255,255,.045);line-height:1;white-space:nowrap}

/* sections */
.section-title{font-size:32px;font-weight:600;line-height:1.25}
.section-title em{font-style:normal;color:var(--red)}
.body-copy{font-size:12.5px;line-height:1.75;color:var(--muted)}
.text-link{display:flex;align-items:center;gap:12px;font-size:12px;font-weight:500;color:#fff}
.circle-btn{position:absolute;width:30px;height:30px;border-radius:50%;border:1px solid var(--line);display:flex;align-items:center;justify-content:center}
.photo{position:absolute;border-radius:6px}

/* news cards */
.news-card{position:absolute;top:1936px;width:312px;height:444px;background:#fff;border-radius:8px;overflow:hidden;color:var(--card-text)}
.news-card .photo{position:relative;border-radius:0;height:256px;width:100%}
.news-body{padding:16px 20px}
.news-date{display:flex;align-items:center;gap:8px;font-size:11px;color:var(--card-muted)}
.news-title{font-size:16px;font-weight:600;margin:12px 0 8px}
.news-text{font-size:11.5px;line-height:1.6;color:var(--card-muted)}
.news-more{position:absolute;right:20px;bottom:16px;display:flex;align-items:center;gap:10px;font-size:11px;font-weight:500;color:var(--card-text)}

/* newsletter */
.newsletter{position:absolute;left:0;top:2520px;width:1200px;height:100px;background:var(--red-deep)}
.newsletter-title{position:absolute;left:80px;top:32px;font-family:'Roboto Slab',serif;font-size:26px;font-weight:400}
.newsletter-input{position:absolute;left:690px;top:30px;width:196px;height:40px;border:1px solid rgba(255,255,255,.25);background:rgba(0,0,0,.2);font-size:12px;color:rgba(255,255,255,.7);padding:12px 14px}
.newsletter-send{position:absolute;left:896px;top:30px;width:70px;height:40px;background:var(--red);font-size:12px;font-weight:500;display:flex;align-items:center;justify-content:center}

/* footer */
.site-footer{position:absolute;left:0;top:2620px;width:1200px;height:384px;overflow:hidden}
.footer-photo{position:absolute;inset:0;background:radial-gradient(ellipse at 60% 45%,#3b3440 0%,#1b1a22 55%,#111015 100%)}
.footer-brand{position:absolute;left:0;width:1200px;top:30px;display:flex;flex-direction:column;align-items:center;gap:10px}
.footer-brand .brand-dot{width:64px;height:64px}
.footer-brand .brand-name{width:auto;font-size:16px;letter-spacing:1px;text-transform:uppercase}
.contact-item{position:absolute;top:190px;width:200px;display:flex;flex-direction:column;align-items:center;gap:14px;font-size:11px;color:var(--muted);text-align:center}
.footer-rule{position:absolute;left:80px;right:80px;top:300px;height:1px;background:var(--line)}
.footer-nav{position:absolute;left:0;width:1200px;top:324px;display:flex;justify-content:center;gap:60px;font-size:12px;color:rgba(255,255,255,.8)}
</style>
</head>
<body>

<section class="hero">
  <div class="hero-photo" role="img" aria-label="Concert crowd with raised hands under red stage lights"></div>
  <p class="hero-eyebrow">Welcome to the orchestra</p>
  <h1 class="hero-title">A <em>Classical</em> youth<br>orchestra</h1>
  <p class="hero-text">Eemstad is the home of young musicians, who understand best the value of music and play in the best environment.</p>
  <a class="btn btn-red" style="left:428px;top:456px;width:152px">Buy Tickets
    <svg width="14" height="14" viewBox="0 0 14 14"><rect x="1" y="3" width="12" height="8" rx="1" fill="none" stroke="#fff" stroke-width="1.4"/></svg></a>
  <a class="btn btn-white" style="left:620px;top:456px;width:160px">Join Orchestra</a>
</section>

<header class="site-header">
  <div class="brand"><span class="brand-dot"></span><span class="brand-name">Eemstad Jeugdorkest</span></div>
  <nav class="main-nav">
    <a class="active">Home</a><a>Orchestras</a><a>Play along</a><a>Concerts</a><a>Tours</a><a>Friends</a><a>Former members</a><a>Contact &amp; Organisation</a>
  </nav>
</header>

<!-- upcoming concert -->
<div class="ghost" style="left:60px;top:690px;font-size:150px">Concert</div>
<h2 class="section-title abs" style="left:120px;top:764px">New Year <em>Concert</em><br>is ahead now</h2>
<p class="body-copy abs" style="left:120px;top:866px;width:400px">Lorem ipsum dolor sit amet, consectetur adipiscing elit, sed do eiusmod tempor incididunt ut labore et dolore magna aliqua.</p>
<p class="body-copy abs" style="left:120px;top:946px;width:400px">Quis ipsum suspendisse ultrices gravida. Risus commodo viverra maecenas accumsan lacus vel facilisis.</p>
<a class="text-link abs" style="left:430px;top:1050px">Buy Tickets
  <svg width="22" height="10" viewBox="0 0 22 10"><path d="M0 5h20M16 1l4 4-4 4" fill="none" stroke="#ec1f27" stroke-width="1.5"/></svg></a>
<span class="circle-btn" style="left:620px;top:860px"><svg width="10" height="10" viewBox="0 0 10 10"><path d="M2 6l3-3 3 3" fill="none" stroke="#fff" stroke-width="1.4"/></svg></span>
<span class="circle-btn" style="left:620px;top:940px"><svg width="10" height="10" viewBox="0 0 10 10"><path d="M2 4l3 3 3-3" fill="none" stroke="#fff" stroke-width="1.4"/></svg></span>
<div class="photo" style="left:832px;top:752px;width:352px;height:320px;background:linear-gradient(135deg,#2a1e1a 0%,#6a3a22 45%,#b57a4a 70%,#1a1414 100%)" role="img" aria-label="Young violinist playing on a dark stage"></div>

<!-- who we are -->
<div class="ghost" style="left:560px;top:1190px;font-size:140px">About us</div>
<div class="photo" style="left:0;top:1140px;width:620px;height:460px;border-radius:0;background:linear-gradient(90deg,#141318 0%,#3a3940 45%,#22212a 80%,rgba(28,27,38,0) 100%)" role="img" aria-label="Studio microphone in soft light"></div>
<div class="photo" style="left:288px;top:1168px;width:192px;height:304px;border-radius:0;background:linear-gradient(160deg,#d9a0a5 0%,#b26a74 50%,#8a4752 100%)" role="img" aria-label="Young musician playing the violin"></div>
<span class="abs" style="left:256px;top:1406px;width:52px;height:52px;border-radius:50%;background:rgba(30,30,40,.85);display:flex;align-items:center;justify-content:center">
  <svg width="16" height="18" viewBox="0 0 16 18"><path d="M2 1l13 8-13 8z" fill="#fff"/></svg></span>
<h2 class="section-title abs" style="left:640px;top:1318px;font-size:34px">Who <em>We</em> Are</h2>
<p class="body-copy abs" style="left:640px;top:1392px;width:340px">Lorem ipsum dolor sit amet, consectetur adipiscing elit, sed do eiusmod tempor incididunt ut labore et dolore magna aliqua.</p>
<p class="body-copy abs" style="left:640px;top:1474px;width:340px">Quis ipsum suspendisse ultrices gravida. Risus commodo viverra maecenas accumsan lacus vel facilisis.</p>
<a class="text-link abs" style="left:780px;top:1560px">Aspiring Musician? Join Now
  <svg width="22" height="10" viewBox="0 0 22 10"><path d="M0 5h20M16 1l4 4-4 4" fill="none" stroke="#ec1f27" stroke-width="1.5"/></svg></a>

<!-- latest news -->
<div class="ghost" style="left:380px;top:1690px;font-size:140px">News</div>
<h2 class="section-title abs" style="left:0;width:1200px;top:1748px;text-align:center;font-size:34px">Our Latest <em>News</em></h2>
<p class="body-copy abs" style="left:370px;top:1818px;width:460px;text-align:center;color:#d6d4de">Lorem ipsum dolor sit amet, consectetur adipiscing elit, sed do eiusmod tempor incididunt ut labore et dolore magna aliqua.</p>
<span class="circle-btn" style="left:922px;top:1772px"><svg width="10" height="10" viewBox="0 0 10 10"><path d="M2 6l3-3 3 3" fill="none" stroke="#fff" stroke-width="1.4"/></svg></span>
<span class="circle-btn" style="left:922px;top:1846px"><svg width="10" height="10" viewBox="0 0 10 10"><path d="M2 4l3 3 3-3" fill="none" stroke="#fff" stroke-width="1.4"/></svg></span>

<article class="news-card" style="left:88px">
  <div class="photo" style="background:linear-gradient(135deg,#f3e9e4 0%,#d9b49a 55%,#7a4a30 100%)" role="img" aria-label="Young violinist on a white background"></div>
  <div class="news-body">
    <p class="news-date"><svg width="14" height="14" viewBox="0 0 14 14"><circle cx="7" cy="7" r="6" fill="none" stroke="#ec1f27" stroke-width="1.4"/><path d="M7 3.5V7l2.5 1.5" fill="none" stroke="#ec1f27" stroke-width="1.4"/></svg>12-11-2019</p>
    <h3 class="news-title">New year concert is ahead</h3>
    <p class="news-text">Lorem ipsum dolor sit amet, consectetur adipiscing elit, sed do eiusmod tempor incididunt ut labore et dolore magna aliqua.</p>
  </div>
  <a class="news-more">Read More <svg width="20" height="10" viewBox="0 0 20 10"><path d="M0 5h18M14 1l4 4-4 4" fill="none" stroke="#ec1f27" stroke-width="1.5"/></svg></a>
</article>

<article class="news-card" style="left:444px">
  <div class="photo" style="background:linear-gradient(135deg,#faf3ea 0%,#e2c08e 55%,#a86a34 100%)" role="img" aria-label="Young musician with violin on a white background"></div>
  <div class="news-body">
    <p class="news-date"><svg width="14" height="14" viewBox="0 0 14 14"><circle cx="7" cy="7" r="6" fill="none" stroke="#ec1f27" stroke-width="1.4"/><path d="M7 3.5V7l2.5 1.5" fill="none" stroke="#ec1f27" stroke-width="1.4"/></svg>12-11-2019</p>
    <h3 class="news-title">New year concert is ahead</h3>
    <p class="news-text">Lorem ipsum dolor sit amet, consectetur adipiscing elit, sed do eiusmod tempor incididunt ut labore et dolore magna aliqua.</p>
  </div>
  <a class="news-more">Read More <svg width="20" height="10" viewBox="0 0 20 10"><path d="M0 5h18M14 1l4 4-4 4" fill="none" stroke="#ec1f27" stroke-width="1.5"/></svg></a>
</article>

<article class="news-card" style="left:796px">
  <div class="photo" style="background:linear-gradient(135deg,#f4f1ee 0%,#c9b8a6 50%,#3a2a24 100%)" role="img" aria-label="Violinist performing on a white background"></div>
  <div class="news-body">
    <p class="news-date"><svg width="14" height="14" viewBox="0 0 14 14"><circle cx="7" cy="7" r="6" fill="none" stroke="#ec1f27" stroke-width="1.4"/><path d="M7 3.5V7l2.5 1.5" fill="none" stroke="#ec1f27" stroke-width="1.4"/></svg>12-11-2019</p>
    <h3 class="news-title">New year concert is ahead</h3>
    <p class="news-text">Lorem ipsum dolor sit amet, consectetur adipiscing elit, sed do eiusmod tempor incididunt ut labore et dolore magna aliqua.</p>
  </div>
  <a class="news-more">Read More <svg width="20" height="10" viewBox="0 0 20 10"><path d="M0 5h18M14 1l4 4-4 4" fill="none" stroke="#ec1f27" stroke-width="1.5"/></svg></a>
</article>

<!-- newsletter -->
<section class="newsletter">
  <h2 class="newsletter-title">Subscribe to our newsletter</h2>
  <div class="newsletter-input">Email</div>
  <div class="newsletter-send">Send</div>
</section>

<!-- footer -->
<footer class="site-footer">
  <div class="footer-photo" role="img" aria-label="Violinist performing in dim light"></div>
  <div class="footer-brand"><span class="brand-dot"></span><span class="brand-name">Eemstad Klassiek</span></div>
  <div class="contact-item" style="left:300px">
    <svg width="26" height="26" viewBox="0 0 24 24"><path d="M6.6 10.8a15 15 0 006.6 6.6l2.2-2.2a1 1 0 011-.25 11.4 11.4 0 003.6.57 1 1 0 011 1V20a1 1 0 01-1 1A17 17 0 013 4a1 1 0 011-1h3.5a1 1 0 011 1c0 1.25.2 2.45.57 3.6a1 1 0 01-.25 1z" fill="#ec1f27"/></svg>
    <span>+31 (0)20 555 01 47</span></div>
  <div class="contact-item" style="left:500px">
    <svg width="26" height="26" viewBox="0 0 24 24"><path d="M12 2a7 7 0 00-7 7c0 5.25 7 13 7 13s7-7.75 7-13a7 7 0 00-7-7zm0 9.5A2.5 2.5 0 1112 6.5a2.5 2.5 0 010 5z" fill="#ec1f27"/></svg>
    <span>Lindelaan 8<br>1234 Eemstad</span></div>
  <div class="contact-item" style="left:700px">
    <svg width="26" height="26" viewBox="0 0 24 24"><rect x="2" y="4" width="20" height="16" rx="2" fill="#ec1f27"/><path d="M3 6l9 7 9-7" fill="none" stroke="#1b1a22" stroke-width="1.6"/></svg>
    <span>info@eemstad-jeugdorkest.example</span></div>
  <div class="footer-rule"></div>
  <nav class="footer-nav"><a>About Us</a><a>Sitemap</a><a>Privacy Disclaimer</a><a>Contact</a></nav>
</footer>

</body>
</html>
```